Boutique Real Estate Brokerage Maplind Realty Website Design

Winning designer work on migrate as well through zip burrow.
We need a new website as an informational hub to aid our print and digital strategy as well as showing that we are located in Brooklyn and Florida. I have a boutique real estate brokerage and advisory firm specializing in residential leasing, multifamily sales and 1031 Exchange appropriation. This won't be a portal to search properties, it will be a place for information. I'd like space for an ebook to be downloaded and information on my probate sales and multifamily leasing marketing campaigns. I included my logo and will leave it up to the designer to come up with colors to match it. I have also attached verbiage for each page. The final design should have a modern high end look that reflects gentrifying Brooklyn as well as beautiful Florida.
Thank you!
Target Market(s)
Owners of income producing real estate and develop-able land in Brooklyn, NY and Florida.
Industry/Entity Type
Real Estate
Coding
Coded - Design and coding required
Number of Pages Required
5+ page
Colors
Designer to choose colors to be used in the design.
Requirements
Must have
- A modern elegant look
Nice to have
- pictures of brooklyn and florida
Should not have
- real estate search pages

```html
<!DOCTYPE html>
<html lang="en">
<head>
<meta charset="utf-8">
<title>Maplind Realty</title>
<link href="https://fonts.googleapis.com/css2?family=Lato:wght@400;700;900&family=Roboto:wght@400;500;700&display=swap" rel="stylesheet">
<style>
  :root {
    --black: #000000;
    --white: #ffffff;
    --ink: #2a2a2a;
    --light-bg: #f4f4f4;
    --band: #2d2d2d;
    --footer: #1e1e1e;
    --bottom: #141414;
    --muted: #d8d8d8;
    --logo-grey: #a9a9a9;
    --accent: #1e7fe0;
    --card-line: #e2e2e2;
  }
  * { margin: 0; padding: 0; box-sizing: border-box; }
  html, body { width: 712px; height: 1200px; overflow: hidden; background: var(--white); }
  body { position: relative; font-family: "Roboto", sans-serif; color: var(--ink); }

  /* Header */
  .site-header { position: absolute; top: 0; left: 0; width: 712px; height: 74px; background: var(--black); }
  .brand { position: absolute; left: 74px; top: 24px; display: flex; align-items: center; gap: 8px; }
  .brand-square { width: 26px; height: 26px; background: var(--logo-grey); }
  .brand-name { font-family: "Lato", sans-serif; font-weight: 700; font-size: 11px; letter-spacing: 2px; color: var(--logo-grey); text-transform: uppercase; }
  .main-nav { position: absolute; top: 29px; left: 320px; display: flex; gap: 15px; align-items: center; }
  .main-nav a { font-family: "Lato", sans-serif; font-weight: 700; font-size: 11px; color: var(--white); text-decoration: none; text-transform: uppercase; }
  .main-nav svg { margin-left: 0; }

  /* Hero */
  .hero { position: absolute; top: 74px; left: 0; width: 712px; height: 356px;
    background: linear-gradient(100deg, #3e4a2e 0%, #5a3424 30%, #3b2018 55%, #6a3222 80%, #2b2a22 100%); }
  .hero::after { content: ""; position: absolute; inset: 0; background: rgba(0,0,0,0.28); }
  .hero-title { position: absolute; z-index: 1; top: 118px; width: 100%; text-align: center; font-family: "Lato", sans-serif; font-weight: 900; font-size: 21px; line-height: 32px; color: var(--white); text-transform: uppercase; text-shadow: 0 2px 4px rgba(0,0,0,0.5); }
  .hero-arrow { position: absolute; z-index: 1; top: 160px; width: 22px; height: 22px; border-radius: 50%; background: rgba(0,0,0,0.55); display: flex; align-items: center; justify-content: center; }
  .hero-arrow.prev { left: 20px; }
  .hero-arrow.next { left: 670px; }
  .scroll-hint { position: absolute; z-index: 1; left: 343px; top: 245px; }

  /* Services */
  .services { position: absolute; top: 430px; left: 0; width: 712px; height: 356px;
    background: linear-gradient(180deg, #fafafa 0%, #eeeeee 100%); }
  .services h2 { position: absolute; top: 62px; width: 100%; text-align: center; font-family: "Lato", sans-serif; font-weight: 700; font-size: 27px; color: #222; text-transform: uppercase; }
  .service-card { position: absolute; top: 126px; width: 180px; height: 158px; background: var(--white); border: 1px solid var(--card-line); box-shadow: 0 1px 4px rgba(0,0,0,0.12); padding: 2px; }
  .service-card .photo { width: 100%; height: 120px; }
  .service-card p { text-align: center; font-family: "Roboto", sans-serif; font-weight: 500; font-size: 12px; margin-top: 12px; color: #333; text-transform: uppercase; }
  .card-1 { left: 66px; } .card-2 { left: 266px; } .card-3 { left: 466px; }
  .photo-kitchen { background: linear-gradient(135deg, #e9e6e0 0%, #bfc3c2 55%, #8c7b68 100%); }
  .photo-building { background: linear-gradient(180deg, #cfd5d8 0%, #7b746c 45%, #4b443d 100%); }
  .photo-aerial { background: linear-gradient(180deg, #9aa6ae 0%, #b7b7a7 35%, #6d7b52 70%, #3f4d3a 100%); }

  /* Tools band */
  .tools { position: absolute; top: 786px; left: 0; width: 712px; height: 157px; background: var(--band); }
  .tool { position: absolute; top: 40px; width: 180px; text-align: center; }
  .tool svg { display: block; margin: 0 auto; }
  .tool h3 { margin-top: 12px; font-family: "Roboto", sans-serif; font-weight: 500; font-size: 15px; color: var(--white); }
  .tool-1 { left: 84px; } .tool-2 { left: 266px; } .tool-3 { left: 449px; }

  /* Footer */
  .site-footer { position: absolute; top: 943px; left: 0; width: 712px; height: 213px; background: var(--footer); color: var(--white); }
  .footer-brand { position: absolute; left: 66px; top: 60px; width: 140px; text-align: center; }
  .footer-brand .brand-square { width: 40px; height: 40px; margin: 0 auto 10px; }
  .footer-brand .brand-name { font-size: 12px; letter-spacing: 2px; }
  .social { position: absolute; left: 76px; top: 157px; display: flex; gap: 9px; }
  .social span { width: 11px; height: 11px; border-radius: 50%; background: var(--white); }
  .footer-col { position: absolute; top: 63px; }
  .footer-col h4 { font-family: "Roboto", sans-serif; font-weight: 500; font-size: 12px; text-transform: uppercase; margin-bottom: 14px; }
  .footer-col ul { list-style: none; }
  .footer-col li { font-size: 9px; line-height: 21px; color: var(--muted); }
  .footer-col li::before { content: "»"; margin-right: 8px; }
  .col-quick { left: 238px; } .col-other { left: 377px; } .col-news { left: 488px; }
  .email-field { width: 157px; height: 22px; background: var(--white); border: 1px solid #ccc; font-size: 7px; color: #555; padding: 6px 8px; margin-top: 2px; }
  .subscribe { width: 72px; height: 23px; margin-top: 8px; border-radius: 12px; background: var(--accent); color: var(--white); font-size: 8px; font-weight: 700; display: flex; align-items: center; justify-content: center; text-transform: uppercase; }

  .bottom-bar { position: absolute; top: 1156px; left: 0; width: 712px; height: 44px; background: var(--bottom); color: var(--white); font-size: 9.5px; text-align: center; line-height: 44px; }
  .bottom-bar .sep { margin: 0 8px; }
</style>
</head>
<body>

<header class="site-header">
  <div class="brand"><span class="brand-square"></span><span class="brand-name">Maplind Realty</span></div>
  <nav class="main-nav">
    <a href="#">Home</a><a href="#">About Us</a><a href="#">Services</a><a href="#">Signup Now</a><a href="#">Contact</a>
    <svg width="10" height="10" viewBox="0 0 10 10"><circle cx="4" cy="4" r="3" fill="none" stroke="#fff" stroke-width="1.6"/><line x1="6.2" y1="6.2" x2="9.3" y2="9.3" stroke="#fff" stroke-width="1.8"/></svg>
  </nav>
</header>

<section class="hero" role="img" aria-label="Photo of a Brooklyn brownstone street with stoops and trees">
  <h1 class="hero-title">Assisting landlords increase profits<br>while decreasing the stress.</h1>
  <span class="hero-arrow prev"><svg width="6" height="8" viewBox="0 0 6 8"><polyline points="4.5,1 1.5,4 4.5,7" fill="none" stroke="#fff" stroke-width="1.3"/></svg></span>
  <span class="hero-arrow next"><svg width="6" height="8" viewBox="0 0 6 8"><polyline points="1.5,1 4.5,4 1.5,7" fill="none" stroke="#fff" stroke-width="1.3"/></svg></span>
  <svg class="scroll-hint" width="26" height="58" viewBox="0 0 26 58">
    <rect x="1.5" y="1" width="23" height="38" rx="11.5" fill="none" stroke="#fff" stroke-width="1.8"/>
    <line x1="13" y1="8" x2="13" y2="16" stroke="#fff" stroke-width="1.8"/>
    <line x1="13" y1="42" x2="13" y2="56" stroke="#fff" stroke-width="1.8"/>
    <polyline points="7,50 13,56 19,50" fill="none" stroke="#fff" stroke-width="1.8"/>
  </svg>
</section>

<section class="services">
  <h2>How we can help</h2>
  <div class="service-card card-1"><div class="photo photo-kitchen" role="img" aria-label="Photo of a bright apartment kitchen and dining area"></div><p>Multi-Family Leasing</p></div>
  <div class="service-card card-2"><div class="photo photo-building" role="img" aria-label="Photo of a multi-family apartment building with fire escapes"></div><p>Multi-Family Sales</p></div>
  <div class="service-card card-3"><div class="photo photo-aerial" role="img" aria-label="Aerial photo of Florida land and a lake"></div><p>Site Selection Advisory</p></div>
</section>

<section class="tools">
  <div class="tool tool-1">
    <svg width="54" height="50" viewBox="0 0 54 50" fill="none" stroke="#fff" stroke-width="2">
      <text x="10" y="18" fill="#fff" stroke="none" font-family="Roboto, sans-serif" font-size="17">$</text>
      <text x="30" y="20" fill="#fff" stroke="none" font-family="Roboto, sans-serif" font-size="17">%</text>
      <path d="M4 36 h12 l10 4 h10 a3 3 0 0 1 0 6 h-14"/>
      <path d="M4 46 h10 l10 3 h18 l8 -14"/>
      <rect x="42" y="28" width="10" height="20"/>
    </svg>
    <h3>Mortgage Rates</h3>
  </div>
  <div class="tool tool-2">
    <svg width="54" height="50" viewBox="0 0 54 50" fill="none" stroke="#fff" stroke-width="2">
      <rect x="8" y="2" width="34" height="46" rx="2"/>
      <rect x="13" y="7" width="24" height="8"/>
      <rect x="13" y="20" width="6" height="6"/><rect x="22" y="20" width="6" height="6"/><rect x="31" y="20" width="6" height="6"/>
      <rect x="13" y="29" width="6" height="6"/><rect x="22" y="29" width="6" height="6"/>
      <rect x="13" y="38" width="6" height="6"/>
      <circle cx="40" cy="38" r="10" fill="#2d2d2d"/>
      <line x1="40" y1="32" x2="40" y2="44"/><line x1="34" y1="38" x2="46" y2="38"/>
    </svg>
    <h3>Mortgage Calculator</h3>
  </div>
  <div class="tool tool-3">
    <svg width="54" height="50" viewBox="0 0 54 50" fill="none" stroke="#fff" stroke-width="2">
      <line x1="20" y1="8" x2="20" y2="46"/>
      <path d="M6 14 h24 l5 4 -5 4 h-24 z"/>
      <path d="M30 26 h-22 l-4 4 4 4 h22 z"/>
      <line x1="12" y1="47" x2="28" y2="47"/>
      <path d="M42 24 c-6 -7 -8 -10 -8 -14 a8 8 0 0 1 16 0 c0 4 -2 7 -8 14 z"/>
      <circle cx="42" cy="10" r="3"/>
    </svg>
    <h3>Coverage Areas</h3>
  </div>
</section>

<footer class="site-footer">
  <div class="footer-brand"><div class="brand-square"></div><span class="brand-name">Maplind Realty</span></div>
  <div class="social"><span></span><span></span><span></span><span></span><span></span><span></span></div>
  <div class="footer-col col-quick">
    <h4>Quick Links</h4>
    <ul><li>Home</li><li>Multi-Family Leasing</li><li>Multi-Family Sales</li><li>Site Selection Advisory</li></ul>
  </div>
  <div class="footer-col col-other">
    <h4>Other Links</h4>
    <ul><li>About Us</li><li>News</li><li>Contact Us</li><li>Terms Of Services</li></ul>
  </div>
  <div class="footer-col col-news">
    <h4>Join Our Newsletter</h4>
    <div class="email-field">Email Address</div>
    <div class="subscribe">Subscribe</div>
  </div>
</footer>

<div class="bottom-bar">Copyright © 2019 Maplind Realty. All Rights Reserved<span class="sep">|</span>Privacy Policy</div>

</body>
</html>
```